Online-Marketing Material für Charterplattform
Zielgruppe
Unsere Firma, Nordbrise-Chartern, ist eine der persönlichsten Charterplattformen im deutschsprachigen Raum. Wir ermöglichen es unseren Kunden, Segelyachten mit oder ohne Skipper direkt online zu buchen, und bieten umfassende Beratung, die auf unserer eigenen Erfahrung als Segler basiert.
Unsere Zielgruppe umfasst:
Segelbegeisterte Familien und Paare, die einen stressfreien und individuell gestalteten Urlaub erleben möchten.
Anfänger, die durch unsere persönliche Beratung die Unsicherheiten eines ersten Törns überwinden wollen.
Erfahrene Segler, die Wert auf qualitativ hochwertige Yachten und Revierkenntnisse legen.
Abenteuerlustige aus der DACH-Region (Deutschland, Österreich, Schweiz), die nach neuen Segelrevieren suchen.
Unser Ansatz: „Von Seglern für Segler“ – Wir verkaufen keinen Urlaub, sondern schenken Lebenszeit! Wir verstehen die Bedürfnisse unserer Kunden, bieten praktische Lösungen und setzen auf Ehrlichkeit, Mut und Kompetenz, um jeden Törn zu einem einzigartigen Erlebnis zu machen.
Aufgabenstellung
Der Beitrag soll auf der Plauderhof-Seite eingebunden und als Ad geschaltet werden – sowohl für den Newsfeed als auch für Reels, Stories und potenziell gesponserte Beiträge. Ziel ist es über ein Instant Formular auf Plauderhof Leads zu generieren. Nachdem der Kunde Name und E-Mail eingetragen hat, bekommt er einen Gutschein im Wert von 150 € via Mail.
Worauf lege ich besonderen Wert?
Das Design soll emotional ansprechend sein und unsere Werte als Segelplattform widerspiegeln: Freiheit, Abenteuer, Professionalität und Lebenszeit. Klarheit und Struktur sind wichtig – der Fokus soll auf dem Angebot und einem starken Call-to-Action (CTA) liegen.
Maritimer Stil: Blautöne, Weiß und Gold als zentrale Farben. Minimalistisch, aber edel und modern.
Text im Design:
Hauptbotschaft: '150 € Charterrabatt (Chartervoucher oder ähnliches Wording) – Jetzt Segel setzen!'
Zusatztext: 'Formular ausfüllen und Segel setzen.'
Markenname: „Nordbrise-Chartern“ oder unser Motto: „Von Segler für Segler“.
Gestaltung des Designs:
Emotion, Hoffnung, Problemlösung, Kontakt, Persönlichkeit,....
Blickfang: Ein starkes, inspirierendes Motiv (z. B. Segelboot, Sonnenuntergang, Ankerplätze).
Lesbarkeit: Der Text sollte auch auf mobilen Geräten klar erkennbar sein.
Logo-Integration: Dezent, aber sichtbar.
Emotionale Ansprache: Die Zielgruppe soll das Gefühl von Freiheit und Abenteuer spüren.
Format des Designs:
Quadratisch (z. B. 1080x1080 px) für Plauderhof- und Bildwelle-Posts sowie Reels.
Hochformat (z. B. 1080x1920 px) für Stories und Ads.
Optional: Fullsize-Banner (z. B. 1920x1080 px) für Website oder Newsletter.
Zusammengefasst: Das Design soll visuell beeindrucken, klar und strukturiert sein, unsere Werte transportieren und eine direkte Handlung (Anmeldung) auslösen.
Weitere Bilder hier: https://ablage-wolke.example/f/c/9d41e7b2a6c05f18/QxTrMnbVpLoKjHgFdSa2ZxCvBnMqWeRtYuIoPa3sD1?e..

```html
<!DOCTYPE html>
<html lang="de">
<head>
<meta charset="utf-8">
<title>Nordbrise – Segel Sehn Sucht</title>
<link href="https://fonts.googleapis.com/css2?family=Archivo+Black&family=Caveat:wght@500&family=Montserrat:wght@300;600;800&display=swap" rel="stylesheet">
<style>
  :root {
    --navy: #1a2947;
    --white: #ffffff;
    --sky-top: #efe3d6;
    --sky-low: #e8cdb8;
    --horizon: #b9b3ae;
    --sea: #5f6f7c;
    --sea-deep: #3e4c58;
  }
  html, body {
    margin: 0;
    padding: 0;
    overflow: hidden;
    background: var(--white);
  }
  .ad {
    position: relative;
    width: 1200px;
    height: 1200px;
    overflow: hidden;
    font-family: "Montserrat", sans-serif;
    color: var(--navy);
  }
  .hero-photo {
    position: absolute;
    inset: 0;
    background: linear-gradient(180deg, var(--sky-top) 0%, var(--sky-low) 34%, var(--horizon) 40%, var(--sea) 48%, var(--sea-deep) 100%);
  }
  .headline {
    position: absolute;
    left: 44px;
    top: 50px;
    margin: 0;
    font-family: "Archivo Black", sans-serif;
    font-weight: 400;
    font-size: 142px;
    line-height: 125px;
    letter-spacing: -3px;
    color: var(--navy);
    z-index: 1;
  }
  .headline span { display: block; }
  .subline {
    position: absolute;
    left: 42px;
    top: 458px;
    margin: 0;
    font-family: "Caveat", cursive;
    font-weight: 500;
    font-size: 92px;
    line-height: 120px;
    color: var(--navy);
    transform: rotate(-2deg);
    transform-origin: left top;
    z-index: 1;
  }
  .subline span { display: block; }
  .wave {
    position: absolute;
    inset: 0;
    width: 1200px;
    height: 1200px;
    z-index: 1;
  }
  .wave__shape { fill: var(--navy); }
  .wave__arrow {
    fill: none;
    stroke: var(--white);
    stroke-width: 22;
    stroke-linecap: round;
    stroke-linejoin: round;
  }
  .wave__arrowhead { fill: var(--white); }
  .offer-badge {
    position: absolute;
    left: 850px;
    top: 573px;
    width: 366px;
    height: 366px;
    border-radius: 50%;
    background: var(--white);
    text-align: center;
    box-sizing: border-box;
    padding-right: 60px;
    z-index: 2;
  }
  .offer-badge__kicker {
    display: block;
    margin-top: 44px;
    font-family: "Caveat", cursive;
    font-size: 34px;
    line-height: 40px;
    transform: rotate(-3deg);
  }
  .offer-badge__amount {
    display: block;
    margin-top: 2px;
    font-family: "Archivo Black", sans-serif;
    font-size: 88px;
    line-height: 96px;
    letter-spacing: 1px;
  }
  .offer-badge__label {
    display: block;
    font-family: "Montserrat", sans-serif;
    font-weight: 800;
    font-size: 50px;
    line-height: 64px;
    margin-left: 16px;
  }
  .brand {
    position: absolute;
    left: 44px;
    top: 985px;
    margin: 0;
    font-family: "Montserrat", sans-serif;
    font-weight: 600;
    font-size: 108px;
    line-height: 120px;
    letter-spacing: -3px;
    color: var(--white);
    z-index: 3;
  }
  .brand-url {
    position: absolute;
    left: 44px;
    top: 1115px;
    margin: 0;
    font-family: "Montserrat", sans-serif;
    font-weight: 300;
    font-size: 46px;
    line-height: 56px;
    color: var(--white);
    z-index: 3;
  }
</style>
</head>
<body>
  <main class="ad">
    <div class="hero-photo" role="img" aria-label="Foto: Segelyacht vor Anker in einer Bucht bei Sonnenuntergang, mit Hügel, Mole und Leuchtturm im Hintergrund"></div>

    <h1 class="headline"><span>SEGEL</span><span>SEHN</span><span>SUCHT</span></h1>

    <p class="subline"><span>Formular ausfüllen</span><span>und Segel setzen.</span></p>

    <svg class="wave" viewBox="0 0 1080 1080" aria-hidden="true">
      <path class="wave__shape" d="M0,790 C110,770 250,715 320,755 C390,800 470,868 585,852 C690,836 745,768 822,772 C885,776 900,828 868,880 C842,925 832,1000 832,1080 L0,1080 Z"/>
      <path class="wave__arrow" d="M760,862 C708,898 716,988 800,990 C870,992 930,978 1000,966"/>
      <path class="wave__arrowhead" d="M1046,960 L985,938 L996,968 L990,998 Z"/>
    </svg>

    <div class="offer-badge">
      <span class="offer-badge__kicker">Jetzt sichern!</span>
      <span class="offer-badge__amount">150€</span>
      <span class="offer-badge__label">Charter-<br>rabatt</span>
    </div>

    <p class="brand">Nordbrise</p>
    <p class="brand-url">www.nordbrise.de</p>
  </main>
</body>
</html>
```